Podcast Cover Art for Fast Growing Show (Ill include a gracious tip!)

This artwork is for "The Steadfast Fellow Show." The podcast is for men, and it's all about self-improvement, confidence, success, money, women and masculinity. It's for the guy who wants to improve himself. I'd like for my picture to be included — in black and white — and I want the text to read: "The Steadfast Fellow Show" and somewhere in there it'll say: "with Dale Prowen." I'm open to color schemes. The podcast is a little edgy so I'd like for that to be represented in the design. Thank you! (((Here's the podcast page if you wanna check it out: http://steadfastfellowshow.castorbit.net/)))

Target Market(s)

Men who want to attract women and improve their lives!

Font styles to use
Serif

Colors

Designer to choose colors to be used in the design.

Requirements
Must have
• My image in it (in black and white) and the two titles: "The Steadfast Fellow Show" and "with Dale Prowen"
Nice to have
• My logo in it somehow (which is the arrow looking logo attached below). I've also found that my image looks best in black and white and with a circular type cut out (although I'm open to different design ideas). I've attached my logo with a circular cut out below so you can see what I'm talking about.
Should not have
• Flowers. Teddy bears. ice cream.

```html
<!DOCTYPE html>
<html lang="en">
<head>
<meta charset="utf-8">
<title>The Steadfast Fellow Show – Cover Art</title>
<link href="https://fonts.googleapis.com/css2?family=Montserrat:wght@300;400;700;800&display=swap" rel="stylesheet">
<style>
  :root {
    --page-bg: #e9ebee;
    --cover-top: #3a3a3a;
    --cover-bottom: #1f1f1f;
    --photo-light: #8a8a8a;
    --photo-dark: #2a2a2a;
    --ink-light: #ffffff;
    --ink-soft: #cfcfcf;
    --ink-dark: #2b2b2b;
  }
  * { box-sizing: border-box; margin: 0; padding: 0; }
  html, body {
    width: 811px;
    height: 1200px;
    overflow: hidden;
    background: var(--page-bg);
    font-family: "Montserrat", Arial, sans-serif;
  }
  .cover {
    position: absolute;
    left: 30px;
    top: 224px;
    width: 751px;
    height: 751px;
    overflow: hidden;
    background: radial-gradient(ellipse at 50% 40%, var(--cover-top) 0%, var(--cover-bottom) 80%);
  }
  .cover-sky {
    position: absolute;
    inset: 0;
    background: radial-gradient(ellipse at 30% 25%, rgba(255,255,255,0.05) 0%, transparent 55%),
                radial-gradient(ellipse at 75% 55%, rgba(255,255,255,0.04) 0%, transparent 50%);
  }
  .host-portrait {
    position: absolute;
    left: 170px;
    top: 85px;
    width: 430px;
    height: 500px;
    border-radius: 210px 210px 40px 40px;
    background: linear-gradient(180deg, var(--photo-light) 0%, #5c5c5c 45%, var(--photo-dark) 100%);
    -webkit-mask-image: linear-gradient(180deg, #000 70%, transparent 100%);
    mask-image: linear-gradient(180deg, #000 70%, transparent 100%);
  }
  .brand-mark {
    position: absolute;
    right: 52px;
    top: 60px;
    display: flex;
    align-items: center;
    gap: 10px;
    color: var(--ink-light);
    font-weight: 800;
    font-size: 26px;
    letter-spacing: 2px;
  }
  .brand-mark-square {
    width: 18px;
    height: 18px;
    background: var(--ink-light);
  }
  .show-title {
    position: absolute;
    left: 178px;
    top: 515px;
    width: 356px;
    height: 195px;
    border-left: 1.5px solid var(--ink-light);
    border-right: 1.5px solid var(--ink-light);
    color: var(--ink-light);
    text-align: center;
  }
  .show-title::before,
  .show-title::after {
    content: "";
    position: absolute;
    top: 0;
    height: 1.5px;
    background: var(--ink-light);
  }
  .show-title::before { left: 0; width: 36%; }
  .show-title::after { right: 0; width: 36%; }
  .show-title-the {
    margin-top: -16px;
    font-weight: 400;
    font-size: 28px;
    line-height: 32px;
    letter-spacing: 1px;
  }
  .show-title-first {
    margin-top: 6px;
    font-weight: 700;
    font-size: 34px;
    line-height: 38px;
    letter-spacing: 0.5px;
  }
  .show-title-main {
    font-weight: 800;
    font-size: 70px;
    line-height: 80px;
    letter-spacing: 1px;
  }
  .show-title-band {
    position: absolute;
    left: -1.5px;
    right: -1.5px;
    bottom: 0;
    height: 32px;
    background: var(--ink-light);
    color: var(--ink-dark);
    font-weight: 300;
    font-size: 21px;
    line-height: 32px;
    letter-spacing: 11px;
    padding-left: 11px;
  }
  .host-credit {
    position: absolute;
    left: 178px;
    top: 718px;
    width: 356px;
    text-align: center;
    color: var(--ink-soft);
    font-weight: 400;
    font-size: 15px;
    line-height: 20px;
    letter-spacing: 3px;
    text-transform: uppercase;
  }
</style>
</head>
<body>
  <main class="cover">
    <div class="cover-sky" aria-hidden="true"></div>

    <div class="host-portrait" role="img" aria-label="Black and white portrait of the host, Dale Prowen, with hands steepled in front of his chin"></div>

    <div class="brand-mark">
      <span class="brand-mark-square"></span>
      <span>STEADFAST</span>
    </div>

    <div class="show-title">
      <p class="show-title-the">THE</p>
      <p class="show-title-first">STEADFAST</p>
      <p class="show-title-main">FELLOW</p>
      <p class="show-title-band">SHOW</p>
    </div>

    <p class="host-credit">with Dale Prowen</p>
  </main>
</body>
</html>
```